The Kestrel Partners Business Cards

We need a sleek looking business card for our real estate company. Looking for a clean, modern, eye catching design on a standard size business card.

No more submissions please! Thank you!

Target Market(s)

General Public/Real Estate Clients

Industry/Entity Type

Real Estate

Contact Information for Business Card

Cards will be customized for each agent.

Colors

Designer to choose only greyscale colors for use in the design.

Requirements
Must have
• Black, white, gray color pallet, Photo area for headshot on the front of the card

```html
<!DOCTYPE html>
<html lang="en">
<head>
<meta charset="utf-8">
<title>The Kestrel Partners — Business Cards</title>
<link href="https://fonts.googleapis.com/css2?family=Montserrat:wght@400;500;600&family=Ubuntu:wght@400;500&family=Roboto:wght@400&display=swap" rel="stylesheet">
<style>
  :root {
    --stage: #2b2b2b;
    --card-back: #262626;
    --card-front: #2f3030;
    --band: #121212;
    --ink: #f2f2f2;
    --ink-soft: #d6d6d6;
    --ink-muted: #a9a9a9;
    --chip: #e4e4e4;
    --chip-ink: #2a2a2a;
    --photo-light: #bdbdbd;
    --photo-mid: #6d625b;
    --photo-dark: #3a3431;
  }
  * { margin: 0; padding: 0; box-sizing: border-box; }
  html, body { width: 1200px; height: 1138px; overflow: hidden; }
  body { background: var(--stage); position: relative; font-family: "Ubuntu", sans-serif; }

  .card {
    position: absolute;
    width: 620px;
    height: 376px;
    border-radius: 14px;
    overflow: hidden;
  }
  .card--back { left: 275px; top: 186px; background: var(--card-back); }
  .card--front { left: 276px; top: 606px; background: var(--card-front); }

  /* back card */
  .back-lockup {
    position: absolute;
    left: 0; right: 0; top: 130px;
    text-align: center;
  }
  .lockup-name {
    font-family: "Montserrat", sans-serif;
    font-weight: 500;
    color: var(--ink);
    font-size: 26px;
    letter-spacing: 6px;
    line-height: 1.35;
  }
  .tag-chip {
    display: inline-block;
    margin-top: 22px;
    background: var(--chip);
    color: var(--chip-ink);
    font-family: "Montserrat", sans-serif;
    font-weight: 600;
    font-size: 10.5px;
    letter-spacing: 2.6px;
    padding: 5px 10px 4px;
  }
  .brokerage {
    position: absolute;
    font-family: "Ubuntu", sans-serif;
    font-weight: 500;
    color: var(--ink-soft);
    font-size: 13px;
    letter-spacing: 0.3px;
  }
  .card--back .brokerage { left: 28px; top: 330px; }

  /* front card */
  .front-lockup {
    position: absolute;
    left: 26px; top: 44px;
    width: 330px;
  }
  .front-lockup .lockup-name { font-size: 24px; letter-spacing: 4px; }
  .front-tagline {
    margin-top: 12px;
    font-family: "Montserrat", sans-serif;
    font-weight: 500;
    color: var(--ink-soft);
    font-size: 14px;
    letter-spacing: 6.5px;
  }
  .agent {
    position: absolute;
    left: 26px; top: 166px;
  }
  .agent-name { color: var(--ink); font-weight: 500; font-size: 25px; }
  .agent-title { color: var(--ink-soft); font-family: "Roboto", sans-serif; font-size: 15px; margin-top: 6px; }
  .agent-phone {
    display: flex; align-items: center; gap: 8px;
    margin-top: 24px;
    color: var(--ink-soft);
    font-family: "Roboto", sans-serif;
    font-size: 18px;
  }
  .card--front .brokerage { left: 26px; top: 292px; }
  .specialty-band {
    position: absolute;
    left: 0; bottom: 0;
    width: 320px; height: 46px;
    background: var(--band);
    color: var(--ink-soft);
    font-family: "Roboto", sans-serif;
    font-size: 15px;
    padding: 13px 0 0 26px;
  }
  .headshot {
    position: absolute;
    right: 0; bottom: 0;
    width: 310px; height: 338px;
    background:
      radial-gradient(ellipse 38% 45% at 55% 42%, var(--photo-mid), transparent 75%),
      linear-gradient(to bottom, transparent 55%, var(--photo-light) 80%),
      linear-gradient(to right, var(--card-front) 0%, var(--photo-dark) 30%, var(--photo-dark) 100%);
  }
</style>
</head>
<body>

  <section class="card card--back">
    <div class="back-lockup">
      <div class="lockup-name">THE KESTREL<br>PARTNERS</div>
      <div class="tag-chip">•REAL ESTATE TEAM•</div>
    </div>
    <div class="brokerage">HARBOR POINT REALTY</div>
  </section>

  <section class="card card--front">
    <div class="front-lockup">
      <div class="lockup-name">THE KESTREL PARTNERS</div>
      <div class="front-tagline">•REAL ESTATE TEAM•</div>
    </div>

    <div class="agent">
      <div class="agent-name">Dana Whitfield Moreno</div>
      <div class="agent-title">Real Estate Broker</div>
      <div class="agent-phone">
        <svg width="20" height="20" viewBox="0 0 24 24" aria-hidden="true">
          <path d="M6.6 10.8a15.2 15.2 0 0 0 6.6 6.6l2.2-2.2c.3-.3.7-.4 1-.2 1.1.4 2.3.6 3.6.6.6 0 1 .4 1 1V20c0 .6-.4 1-1 1A17 17 0 0 1 3 4c0-.6.4-1 1-1h3.5c.6 0 1 .4 1 1 0 1.3.2 2.5.6 3.6.1.3 0 .7-.2 1z" fill="none" stroke="#d6d6d6" stroke-width="1.8"/>
        </svg>
        <span>+1 555-302-7719</span>
      </div>
    </div>

    <div class="brokerage">HARBOR POINT REALTY</div>

    <div class="headshot" role="img" aria-label="Agent headshot photo"></div>
    <div class="specialty-band">RESIDENTIAL REAL ESTATE</div>
  </section>

</body>
</html>
```